Harbor Lanterns: Walking Beside Young Ones Through Every Season

This book is about being a good father and how to parent them well so they are fully equipped to launch into the world when they become adults. It is an encouraging and practical guide that acknowledges the difficulties of being a good father and provides strategies for addressing them.

Target Market(s)

My target market is dads, or people that will gift this book to a dad that they know

```html
<!DOCTYPE html>
<html lang="en">
<head>
<meta charset="utf-8">
<title>Harbor Lanterns: Walking Beside Young Ones Through Every Season</title>
<link rel="stylesheet" href="https://fonts.googleapis.com/css2?family=Barlow+Condensed:wght@700&family=Montserrat:wght@900&family=Poppins:wght@600&display=swap">
<style>
  :root {
    --backdrop: #d4d3d8;
    --plum: #8e387c;
    --rose: #b8416a;
    --coral: #e0524a;
    --tangerine: #e5834a;
    --sun: #e6c446;
    --ink: #111111;
    --paper: #f4f4f6;
    --sky: #6ab6e4;
    --gold: #ecb83a;
  }
  * { margin: 0; padding: 0; box-sizing: border-box; }
  html, body {
    width: 1200px;
    height: 1000px;
    overflow: hidden;
    background: var(--backdrop);
  }
  .canvas {
    position: relative;
    width: 1200px;
    height: 1000px;
  }
  .book-cover {
    position: absolute;
    left: 327px;
    top: 50px;
    width: 546px;
    height: 900px;
    overflow: hidden;
    background: linear-gradient(180deg,
      var(--plum) 0%,
      var(--rose) 28%,
      var(--coral) 58%,
      var(--tangerine) 78%,
      var(--sun) 100%);
  }
  .cover-wave {
    position: absolute;
    left: 0;
    top: 0;
    width: 546px;
    height: 900px;
  }
  .title-lead {
    position: absolute;
    left: 152px;
    top: 148px;
    font-family: "Barlow Condensed", sans-serif;
    font-weight: 700;
    font-size: 62px;
    line-height: 62px;
    color: var(--paper);
    text-transform: uppercase;
  }
  .title-verb {
    position: absolute;
    left: 158px;
    top: 284px;
    font-family: "Barlow Condensed", sans-serif;
    font-weight: 700;
    font-size: 43px;
    line-height: 50px;
    color: var(--ink);
    text-transform: uppercase;
    white-space: nowrap;
  }
  .title-hero {
    position: absolute;
    left: 23px;
    top: 380px;
    width: 500px;
    height: 230px;
    display: flex;
    justify-content: center;
    align-items: center;
    font-family: "Montserrat", sans-serif;
    font-weight: 900;
    font-size: 148px;
    line-height: 230px;
    letter-spacing: -6px;
    color: var(--paper);
    text-transform: uppercase;
    white-space: nowrap;
  }
  .title-close {
    position: absolute;
    left: 84px;
    top: 634px;
    font-family: "Barlow Condensed", sans-serif;
    font-weight: 700;
    font-size: 46px;
    line-height: 50px;
    color: var(--ink);
    text-transform: uppercase;
    white-space: nowrap;
  }
  .art-hat {
    position: absolute;
    left: 24px;
    top: 268px;
    width: 122px;
    height: 110px;
    border-radius: 50% 50% 45% 45%;
    background: var(--sky);
  }
  .art-moustache {
    position: absolute;
    left: 64px;
    top: 384px;
    width: 92px;
    height: 42px;
    border-radius: 30px;
    background: var(--gold);
  }
  .art-tie {
    flex: 0 0 auto;
    width: 34px;
    height: 150px;
    margin: 0 12px 0 10px;
    border-radius: 8px 8px 20px 20px;
    background: var(--sky);
  }
  .author-name {
    position: absolute;
    left: 0;
    top: 836px;
    width: 546px;
    text-align: center;
    font-family: "Poppins", sans-serif;
    font-weight: 600;
    font-size: 23px;
    line-height: 30px;
    color: var(--ink);
  }
</style>
</head>
<body>
  <main class="canvas">
    <section class="book-cover">
      <svg class="cover-wave" viewBox="0 0 546 900" aria-hidden="true">
        <path d="M0 708 Q 200 730 546 676 L 546 900 L 0 900 Z" fill="#f0b448" opacity="0.28"/>
      </svg>

      <h1 class="title-lead">Harbor<br>Lanterns:</h1>
      <p class="title-verb">Walking Beside Young</p>
      <p class="title-hero" aria-label="Ones"><span aria-hidden="true">O</span><span class="art-tie" role="img" aria-label="Illustration of a blue necktie"></span><span aria-hidden="true">NES</span></p>
      <p class="title-close">Through Every Season</p>

      <div class="art-hat" role="img" aria-label="Illustration of a blue fedora hat with a gold band"></div>
      <div class="art-moustache" role="img" aria-label="Illustration of a golden moustache"></div>

      <p class="author-name">Author Book</p>
    </section>
  </main>
</body>
</html>
```